Film Poster Design For Japanese Film Poster #2

The title of this colour film is KUMO TORI MIZU HOSHI春 夏 秋 冬Translated this is literallySpring Summer Fall Winter ... however the English title is FOUR SEASONSWe attached a series of screen shots from the film and also the computer generated Kanji characters. We will be updating the brief with the Japanese title characters which currently being hand painted.We require the post in two formats. One being the traditional poster format and the other being in a wide screen ration of 1000px by 465px. Same design.This is a drama, feature length film comprising of four separate stories. The is mixture of Japanese and English dialogue. We are looking at 2 possible designs. You can choose to submit either.1: A with lots of white space ... focussing on smaller images at the Japanese text. I have uploaded a sample poster as a very rough indication. "Words nobody says while crossing the bridge" / "Odile Petra June Beaudry" - Lots of white space.Ideally we would have liked to have had the image of the young girl in the kimono pulling on the bell rope clear cut and used on white as a single main image. However, we are not sure that the clarity or resolution of the original image is sufficient. 2: One with lots of images as you can see with the two "Glass Of Rain" Sample posters.Obviously we are not looking for a copy of either poster, but these posters are a guide to the two looks we are after.Thanks. Mayuko
Hello all,Apologies for the delay. We have had to work through some naming issues.The film's English title has had to be renamed to THE LANTERNS. Please do not used PALE HARBOUR in any designed moving forward.Thanks Mayuko Added Sunday, May 25, 2014

```html
<!DOCTYPE html>
<html lang="en">
<head>
<meta charset="utf-8">
<title>KUMO TORI MIZU HOSHI — THE LANTERNS</title>
<link rel="stylesheet" href="https://fonts.googleapis.com/css2?family=Noto+Sans+JP:wght@900&family=Oswald:wght@400;600&display=swap">
<style>
  :root {
    --paper: #ffffff;
    --ink: #111111;
    --band-red: #ee1c1c;
    --word-green: #8bd12c;
    --word-yellow: #ffe21a;
    --word-orange: #f7a13a;
    --word-white: #ffffff;
  }
  html, body {
    margin: 0;
    padding: 0;
    overflow: hidden;
    background: var(--paper);
  }
  .poster {
    position: relative;
    width: 848px;
    height: 1200px;
    background: var(--paper);
    overflow: hidden;
  }
  .kanji {
    position: absolute;
    margin: 0;
    font-family: "Noto Sans JP", sans-serif;
    font-weight: 900;
    font-size: 300px;
    line-height: 1;
    color: transparent;
    -webkit-background-clip: text;
    background-clip: text;
  }
  .kanji--cloud {
    left: 84px; top: 72px;
    background-image: linear-gradient(180deg, #3d4a33 0%, #6d6a58 40%, #4f5e48 60%, #3f7a2e 100%);
  }
  .kanji--bird {
    left: 420px; top: 72px;
    background-image: linear-gradient(180deg, #b8a071 0%, #d7a45c 30%, #3a2a1a 55%, #7a5a36 75%, #1e1a14 100%);
  }
  .kanji--river {
    left: 84px; top: 560px;
    background-image: linear-gradient(160deg, #a3341c 0%, #c2542a 30%, #5b6b2a 60%, #2f4a1f 100%);
  }
  .kanji--star {
    left: 420px; top: 560px;
    transform: rotate(-4deg);
    background-image: linear-gradient(180deg, #4a5a62 0%, #1f3a2a 40%, #22302a 60%, #4b7ec8 85%, #5a8fd8 100%);
  }
  .title-band {
    position: absolute;
    left: 0;
    top: 452px;
    width: 848px;
    height: 48px;
    background: var(--band-red);
  }
  .title-band__words {
    position: absolute;
    left: 80px;
    top: 0;
    margin: 0;
    font-family: "Oswald", sans-serif;
    font-weight: 600;
    font-size: 36px;
    line-height: 48px;
    letter-spacing: 0.5px;
    white-space: nowrap;
  }
  .word--green { color: var(--word-green); }
  .word--yellow { color: var(--word-yellow); }
  .word--orange { color: var(--word-orange); }
  .word--white { color: var(--word-white); }
  .still-frame {
    position: absolute;
    left: 665px;
    top: 406px;
    width: 144px;
    height: 144px;
  }
  .synopsis {
    position: absolute;
    left: 122px;
    top: 950px;
    width: 608px;
    margin: 0;
    font-family: "Oswald", sans-serif;
    font-weight: 400;
    font-size: 12.4px;
    line-height: 15.6px;
    text-transform: uppercase;
    text-align: justify;
    color: var(--ink);
  }
</style>
</head>
<body>
  <main class="poster">
    <h1 class="kanji kanji--cloud" lang="ja" aria-label="雲">雲</h1>
    <p class="kanji kanji--bird" lang="ja">鳥</p>
    <p class="kanji kanji--river" lang="ja">水</p>
    <p class="kanji kanji--star" lang="ja">星</p>

    <div class="title-band">
      <p class="title-band__words">
        <span class="word--green">KUMO</span>
        <span class="word--yellow">TORI</span>
        <span class="word--orange">MIZU</span>
        <span class="word--white">HOSHI</span>
      </p>
    </div>

    <svg class="still-frame" viewBox="0 0 144 144" aria-hidden="false">
      <defs>
        <linearGradient id="still-tones" x1="0" y1="0" x2="0" y2="1">
          <stop offset="0" stop-color="#5a5448"/>
          <stop offset="0.55" stop-color="#3b3630"/>
          <stop offset="1" stop-color="#6a6258"/>
        </linearGradient>
      </defs>
      <circle cx="72" cy="72" r="72" fill="var(--band-red)"/>
      <circle cx="72" cy="72" r="56" fill="url(#still-tones)" role="img" aria-label="Film still: a young girl in a kimono pulling a temple bell rope"/>
    </svg>

    <p class="synopsis">
      Lorem ipsum dolor sit amet, in inermis dolorem legendos nec. Ad integre constituto mei, vim eu detracto deseruisse. Sea soleat aeterno id, sanctus mandamus ei eam. Duo te mundi errem legimus, cibo quando meliore mea eu. Eos iusto sonet periculis ea. Cum ea quando platonem, at his volumus forensibus. Lorem ipsum dolor sit amet, in inermis dolorem legendos nec. Ad integre constituto mei, vim eu detracto deseruisse. Sea soleat aeterno id, sanctus mandamus ei eam. Duo te mundi errem legimus, cibo quando meliore mea eu. Eos iusto sonet periculis ea. Cum ea quando platonem, at his volumus forensibus. Lorem ipsum dolor sit amet, in inermis dolorem legendos nec. Ad integre constituto mei, vim eu detracto deseruisse. Sea soleat aeterno id, sanctus mandamus ei eam. Duo te mundi errem legimus, cibo quando meliore mea eu. Eos iusto sonet periculis ea. Cum ea quando platonem, at his volumus forensibus.
    </p>
  </main>
</body>
</html>
```